BROCHURE DESIGN WINDOW VORELTA

We need a brochure for our VORELTA window shutters. The information we need to contain the brochure is in the attachment. The initial idea is a size A4 format (letter) folded in 3 leaves but are open to sujerencias and other formats. For more information visit the website: WWW.VORELTA-EXAMPLE.COM.DO We need a brochure for our VORELTA window. The information we need to Contain the brochure is in the attachment. The initial concept is a size A4 format (letter) folded in three leaves but are open to other formats. For more information visit the website: WWW.VORELTA-EXAMPLE.COM.DO

Target Market(s)

window manufacturers and end users.

Font styles to use
Sans Serif

Requirements
Nice to have
• 2 versions of brochure; English and Spanish language versions 2; spanish / Inglés

```html
<!DOCTYPE html>
<html lang="es">
<head>
<meta charset="utf-8">
<title>Folleto VORELTA celosías</title>
<link href="https://fonts.googleapis.com/css2?family=Arimo:ital,wght@0,400;0,700;1,400&display=swap" rel="stylesheet">
<style>
:root{
  --paper:#dfe9cb;
  --orange:#e0813e;
  --brick:#a9482e;
  --navy:#2c2d3e;
  --title:#d0161b;
  --ink:#111;
  --table-grey:#b9b9bd;
  --table-light:#e9e9ec;
}
*{margin:0;padding:0;box-sizing:border-box}
html,body{width:1200px;height:1006px;overflow:hidden;background:var(--paper)}
body{font-family:'Arimo',Arial,sans-serif;color:var(--ink);position:relative}
.bands{position:absolute;left:0;top:0}
.panel{position:absolute;top:0;width:400px;height:1006px}
.panel--left{left:0}
.panel--mid{left:400px;border-left:1px solid rgba(0,0,0,.06)}
.panel--right{left:800px;border-left:1px solid rgba(0,0,0,.06)}
.abs{position:absolute}
.section-title{position:absolute;color:var(--title);font-style:italic;font-size:16px;white-space:nowrap;transform:translateX(-50%)}
.center{text-align:center;transform:translateX(-50%);white-space:nowrap}
.photo{position:absolute}
.model-photo{background:linear-gradient(135deg,#f4f3ea,#cfd0c4);border:2px solid #c9c9bd}
.caption{font-size:11px}
.fine{font-size:6.5px;line-height:9px;text-align:center;position:absolute}
.body-copy{font-size:11.5px;line-height:14px}
.swatch{position:absolute}
.list{position:absolute;font-size:12.5px;line-height:23.5px;text-align:center;transform:translateX(-50%);white-space:nowrap}
.config-label{position:absolute;font-size:12px;line-height:23.5px}
.config-label b{font-style:italic;display:block}
.config-art{position:absolute;background:linear-gradient(135deg,#6b6f6c,#2f3230)}
.heights{position:absolute;left:27px;top:573px;width:340px;height:403px;border:5px solid #1b1b1f;background:var(--table-light);border-collapse:collapse;font-weight:700;font-size:8px;text-align:center}
.heights th,.heights td{border:1px solid #333;padding:0;line-height:12px}
.heights thead th{background:var(--table-grey);font-size:8px;line-height:9px}
.heights td:first-child{background:var(--table-grey)}
.footer-note{position:absolute;left:200px;top:924px;font-size:10px;line-height:13px;text-align:center;transform:translateX(-50%);white-space:nowrap}
</style>
</head>
<body>
<svg class="bands" width="1200" height="170" viewBox="0 0 1200 170" aria-hidden="true">
  <polygon points="0,0 720,0 720,10 410,60 0,145" fill="var(--orange)"/>
  <polygon points="410,40 720,10 1000,0 1060,0 820,48 820,60 410,168" fill="var(--brick)"/>
  <polygon points="820,48 1060,0 1200,0 1200,8 820,145" fill="var(--navy)"/>
</svg>

<section class="panel panel--left">
  <h2 class="section-title" style="left:216px;top:126px;font-weight:400">Modelos</h2>
  <div class="photo model-photo" role="img" aria-label="Ventana de celosías VORELTA Heavy Duty" style="left:59px;top:157px;width:115px;height:280px"></div>
  <div class="photo model-photo" role="img" aria-label="Ventana de celosías VORELTA Standard Duty" style="left:237px;top:157px;width:135px;height:280px"></div>
  <p class="abs caption center" style="left:116px;top:445px">VORELTA Heavy Duty, (UHD)</p>
  <p class="abs caption center" style="left:304px;top:447px">VORELTA Standard Duty, (USD)</p>
  <p class="fine" style="left:20px;top:473px;width:190px">Maxima calidad y resistencia porque sus celosias son tubulares. La celosias ademas incorporan entre si una junta de goma o felpa.</p>
  <p class="fine" style="left:218px;top:476px;width:170px">Es el modelo economico. Sus celosias son muy resistentes pero no son tubulares. Ofrece una excelente relacion cal Vidad/precio.</p>
  <p class="abs body-copy" style="left:0;width:400px;text-align:center;top:525px">VORELTA no son solo ventanas de marco fijo,<br>tambien estan diponibles puertas y ventanas abisagradas</p>
  <div class="photo" role="img" aria-label="Mano sosteniendo un control remoto" style="left:9px;top:597px;width:200px;height:200px;border-radius:50%;background:radial-gradient(circle,#e4e2d8,#8a8d86)"></div>
  <h2 class="section-title" style="left:283px;top:628px;font-weight:400">Accionamientos</h2>
  <div class="photo" role="img" aria-label="Operador manual de mariposa en una ventana de celosías" style="left:225px;top:693px;width:150px;height:211px;background:linear-gradient(160deg,#5a5c55,#c8c9c0 45%,#3d3f3a)"></div>
  <p class="fine" style="left:4px;top:820px;width:200px;font-size:7.5px;line-height:10px">Automatico: pulsador, control remoto,<br>tableta/movil o bien atraves de sistema domotico.</p>
  <div class="photo" role="img" aria-label="Pulsador de pared negro" style="left:0;top:877px;width:108px;height:108px;border-radius:50%;background:radial-gradient(circle,#3a3a3a,#0d0d0d)"></div>
  <p class="abs caption center" style="left:292px;top:918px;font-size:10px">Manual: Operador de mariposa</p>
</section>

<section class="panel panel--mid">
  <div class="swatch" style="left:14px;top:197px;width:66px;height:188px;background:linear-gradient(#f3f3f0,#d8d8d4)"></div>
  <div class="swatch" style="left:91px;top:166px;width:64px;height:187px;background:linear-gradient(#c9c9cb,#97989c)"></div>
  <div class="swatch" style="left:173px;top:134px;width:64px;height:191px;background:#2a1510"></div>
  <h2 class="section-title" style="left:310px;top:184px;font-weight:400">Standard</h2>
  <p class="list" style="left:308px;top:224px;font-size:12px;line-height:23.5px">Lacado Blanco<br>Anodizado Plata Mate<br>Anodizado Bronce Claro</p>
  <div class="swatch" style="left:14px;top:425px;width:66px;height:196px;background:#232328"></div>
  <div class="swatch" style="left:108px;top:393px;width:66px;height:194px;background:linear-gradient(#e4ded4,#8e877c)"></div>
  <div class="swatch" style="left:206px;top:357px;width:67px;height:197px;background:#3a1420"></div>
  <div class="swatch" style="left:300px;top:337px;width:69px;height:196px;background:#2b2c3f"></div>
  <h2 class="section-title" style="left:281px;top:567px;font-weight:400">Especiales</h2>
  <p class="list" style="left:267px;top:603px;font-size:12px">Disponibles todos los colores de la<br>gama CROMA, (lacados o anodizados).<br>Tambien imitaciones acero inoxidable</p>
  <div class="photo" role="img" aria-label="Abanico de muestras de acabado imitación madera" style="left:3px;top:673px;width:214px;height:239px;background:radial-gradient(circle,#a5532a,#5a2418 60%,transparent 72%)"></div>
  <h2 class="section-title" style="left:290px;top:735px;font-weight:400">Imitacion madera</h2>
  <p class="list" style="left:290px;top:773px;font-size:12px">Roble, cerezo, caoba,<br>y muchas mas.<br>Todos ellos incluyer<br>vetas con textura</p>
  <p class="footer-note">Todos los acabados superficiates estan garantizados por 10 anos.<br>Ademas cuentan con los sellos intenacionales de calidad<br>“Label Coatmark” para lacados y “Label Anodmark” para Anodizados.</p>
</section>

<section class="panel panel--right">
  <h2 class="section-title" style="left:25px;top:144px;font-weight:400;transform:none">Configuraciones</h2>
  <p class="abs body-copy" style="left:25px;top:172px;width:360px;line-height:14px">Las configuraciones vienen determinados por las divisiones verticales y horizontales de la ventana</p>
  <p class="abs body-copy" style="left:25px;top:216px;line-height:13px">Divisiones verticales: Cuerpos<br>Divisiones horizontales: Modulos</p>
  <p class="abs body-copy" style="left:25px;top:253px;width:360px;line-height:14px">Pueden fabricarse multiples configuraciones. Estos son las mas comunes</p>

  <p class="config-label" style="left:33px;top:300px"><b>1x1</b>1 cuerpo<br>1 modulo<br>1 operador</p>
  <div class="config-art" role="img" aria-label="Ventana de un cuerpo y un módulo" style="left:107px;top:303px;width:48px;height:90px"></div>
  <p class="config-label" style="left:203px;top:303px"><b>2x1</b>2 cuerpos<br>1 modulo<br>2 operadores</p>
  <div class="config-art" role="img" aria-label="Ventana de dos cuerpos y un módulo" style="left:278px;top:283px;width:97px;height:120px"></div>
  <p class="config-label" style="left:30px;top:446px"><b>1x2</b>1 cuerpo<br>2 modulos<br>2 operadores</p>
  <div class="config-art" role="img" aria-label="Ventana de un cuerpo y dos módulos" style="left:109px;top:433px;width:43px;height:120px"></div>
  <p class="config-label" style="left:203px;top:449px"><b>2x2</b>2 cuerpos<br>2 modulos<br>4 operadores</p>
  <div class="config-art" role="img" aria-label="Ventana de dos cuerpos y dos módulos" style="left:285px;top:399px;width:81px;height:154px"></div>

  <table class="heights">
    <thead>
      <tr><th rowspan="2" style="width:30%">CANTIDAD DE<br>CELOSIAS</th><th colspan="2">ALTURAS ESTANDAR DE VENTANA</th></tr>
      <tr><th>Metros</th><th>Pulgadas</th></tr>
    </thead>
    <tbody>
      <tr><td>3</td><td>0,311</td><td>12 1/4</td></tr>
      <tr><td>4</td><td>0,400</td><td>15 3/4</td></tr>
      <tr><td>5</td><td>0,489</td><td>19 1/4</td></tr>
      <tr><td>6</td><td>0,578</td><td>22 3/4</td></tr>
      <tr><td>7</td><td>0,667</td><td>26 1/4</td></tr>
      <tr><td>8</td><td>0,756</td><td>29 3/4</td></tr>
      <tr><td>9</td><td>0,845</td><td>33 1/4</td></tr>
      <tr><td>10</td><td>0,934</td><td>36 3/4</td></tr>
      <tr><td>11</td><td>1,023</td><td>40 1/4</td></tr>
      <tr><td>12</td><td>1,112</td><td>43 3/4</td></tr>
      <tr><td>13</td><td>1,201</td><td>47 1/4</td></tr>
      <tr><td>14</td><td>1,290</td><td>50 3/4</td></tr>
      <tr><td>15</td><td>1,379</td><td>54 1/4</td></tr>
      <tr><td>16</td><td>1,468</td><td>57 3/4</td></tr>
      <tr><td>17</td><td>1,557</td><td>61 1/4</td></tr>
      <tr><td>18</td><td>1,646</td><td>64 3/4</td></tr>
      <tr><td>19</td><td>1,735</td><td>68 1/4</td></tr>
      <tr><td>20</td><td>1,824</td><td>71 3/4</td></tr>
      <tr><td>21</td><td>1,913</td><td>75 1/4</td></tr>
      <tr><td>22</td><td>2,002</td><td>78 3/4</td></tr>
      <tr><td>23</td><td>2,091</td><td>82 1/4</td></tr>
      <tr><td>24</td><td>2,180</td><td>85 3/4</td></tr>
      <tr><td>25</td><td>2,269</td><td>89 1/4</td></tr>
      <tr><td>26</td><td>2,358</td><td>92 3/4</td></tr>
      <tr><td>27</td><td>2,447</td><td>96 1/4</td></tr>
      <tr><td>28</td><td>2,536</td><td>99 3/4</td></tr>
      <tr><td>29</td><td>2,625</td><td>103 1/4</td></tr>
      <tr><td>30</td><td>2,714</td><td>106 3/4</td></tr>
    </tbody>
  </table>
</section>
</body>
</html>
```